Maple Sprout Menu (Vegetarian Restaurant Concept)

Maple Sprout is a new concept fast casual restaurant
renders are attached so you can see the style of restaurant
Maple Sproutt is a vibrant and modern Vegetarian fast casual restaurant concept that mixes fresh food, energy, great décor, and a comfortable, welcoming atmosphere to provide a memorable and all Vegetarian dining experience.
Our Mission is to be top of mind when consumers think Vegetarian food!
Target Market(s)
the menu is vegetarian and appeals to a broad demographic in USA
Colors
Designer to choose colors to be used in the design.
Requirements
Must have
- well colored and well laid out menu - should not be cartoonish
Nice to have
- For Phots please use the shots in this file:
- https://www.filecrate-example.com/sh/qwx7tr2bnm4kdle/BBBdK_pQrLmNZTHO5E_XYZ_Kb?dl=0
- note these are untouched and you are free to change as needed
Should not have
- Should not be cartoonish - nor kives, forks etc in the design

```html
<!DOCTYPE html>
<html lang="en">
<head>
<meta charset="utf-8">
<title>Maple Sprout Menu</title>
<link rel="stylesheet" href="https://fonts.googleapis.com/css2?family=Abril+Fatface&display=swap">
<style>
  :root {
    --paper: #ffffff;
    --panel: #212427;
    --ink-light: #ffffff;
    --leaf: #5d9a3c;
    --hairline: #e6e6e6;
    --salad-tone: #5f7a3a;
    --salad-tone-2: #8aa24e;
    --caesar-tone: #a9b86a;
    --caesar-tone-2: #c9a564;
  }
  * { margin: 0; padding: 0; box-sizing: border-box; }
  html, body { width: 848px; height: 1200px; overflow: hidden; background: var(--paper); }
  .menu-page {
    position: relative; width: 848px; height: 1200px; overflow: hidden;
    background: var(--paper);
    font-family: "Abril Fatface", Georgia, serif;
  }
  .photo-column { position: absolute; left: 0; top: 0; width: 300px; height: 1200px; }
  .photo-column svg { position: absolute; left: 0; top: 0; }
  .menu-panel {
    position: absolute; left: 300px; top: 0; width: 548px; height: 1200px;
    background: var(--panel); color: var(--ink-light);
  }
  .menu-title {
    position: absolute; left: 0; width: 548px; top: 32px;
    text-align: center; font-size: 84px; line-height: 1; letter-spacing: -1px;
  }
  .section-heading {
    position: absolute; left: 45px; font-size: 50px; line-height: 1; letter-spacing: -0.5px;
  }
  .section-rule {
    position: absolute; left: 43px; width: 465px; height: 2px; background: var(--ink-light);
  }
  .dish { position: absolute; left: 45px; width: 470px; }
  .dish-name { font-size: 24px; line-height: 32px; letter-spacing: -0.3px; }
  .dish-desc { color: var(--leaf); font-size: 16px; line-height: 21px; margin-top: 5px; letter-spacing: -0.2px; }
</style>
</head>
<body>
<main class="menu-page">
  <aside class="photo-column">
    <svg width="300" height="1200" viewBox="0 0 300 1200">
      <defs>
        <radialGradient id="mixedGreens" cx="0.4" cy="0.5" r="0.6">
          <stop offset="0" stop-color="var(--salad-tone-2)"/>
          <stop offset="1" stop-color="var(--salad-tone)"/>
        </radialGradient>
        <radialGradient id="caesarGreens" cx="0.4" cy="0.5" r="0.6">
          <stop offset="0" stop-color="var(--caesar-tone-2)"/>
          <stop offset="1" stop-color="var(--caesar-tone)"/>
        </radialGradient>
      </defs>
      <circle cx="18" cy="309" r="242" fill="url(#mixedGreens)" role="img" aria-label="Photo of mixed green salad with avocado, cherry tomatoes, almonds, goat cheese and balsamic drizzle"/>
      <rect x="0" y="626" width="230" height="1" fill="var(--hairline)"/>
      <circle cx="18" cy="895" r="242" fill="url(#caesarGreens)" role="img" aria-label="Photo of shaved brussel sprout caesar with croutons, dried cranberries, parmesan and lemon"/>
    </svg>
  </aside>

  <section class="menu-panel">
    <h1 class="menu-title">MENU</h1>

    <h2 class="section-heading" style="top:182px">SALADS</h2>
    <div class="section-rule" style="top:235px"></div>

    <article class="dish" style="top:266px">
      <h3 class="dish-name">Brussel Sprout Ceasar</h3>
      <p class="dish-desc">little gem romaine, toasted torn bread,<br>parmigiano reggiano</p>
    </article>
    <article class="dish" style="top:366px">
      <h3 class="dish-name">Heirloom Beet Salad</h3>
      <p class="dish-desc">shaved chioggia beet, roasted golden beet,<br>red quinoa, little gem, arugula, lemon vinaigrette</p>
    </article>
    <article class="dish" style="top:466px">
      <h3 class="dish-name">Zesty Black Bean &amp;<br>Corn Salad in Lettuce Cups</h3>
      <p class="dish-desc">black beans, avocado and roasted corn topped<br>with feta crumbles in butter lettuce</p>
    </article>
    <article class="dish" style="top:597px">
      <h3 class="dish-name">Green, Red and White</h3>
      <p class="dish-desc">spring leaves, cherry tomatoes, avocado,<br>roasted almond and goat cheese</p>
    </article>

    <h2 class="section-heading" style="top:737px">TOASTS</h2>
    <div class="section-rule" style="top:791px"></div>

    <article class="dish" style="top:816px">
      <h3 class="dish-name">Everything Avocado Toast</h3>
      <p class="dish-desc">avocado on whole grain toast with our<br>signature spice blend</p>
    </article>
    <article class="dish" style="top:916px">
      <h3 class="dish-name">Tomato &amp; Beet Bruschetta</h3>
    </article>
    <article class="dish" style="top:962px">
      <h3 class="dish-name">Vegetable Melt on Garlic Toast</h3>
    </article>

    <h2 class="section-heading" style="top:1047px">SOUP</h2>
    <div class="section-rule" style="top:1101px"></div>

    <article class="dish" style="top:1136px">
      <h3 class="dish-name">Black Bean Chowder</h3>
    </article>
  </section>
</main>
</body>
</html>
```